New world-class investment firm needs a business card design

We need a business card design for a new investment firm called 'Dalvin Soeurs & Company.' We acquire companies in the media sector and secure funding from conservative ultra, high-net worth individuals. We would like a black and white color design. We are seeking classic, elegant, and sophisticated designs. The final design should communicate financial safety, class, timelessness, and highly ethical. On the back of the business card, we would simply like the lion logo to be centered. I have attached a mock card, and variations on it are welcomed.
Industry/Entity Type
Conservative
Font styles to use
Other font styles liked:
- Garamond
Look and feel
Each slider illustrates characteristics of the customer's brand and the style your logo design should communicate.

```html
<!DOCTYPE html>
<html lang="en">
<head>
<meta charset="utf-8">
<title>Dalvin Soeurs &amp; Company – Business Card</title>
<link rel="stylesheet" href="https://fonts.googleapis.com/css2?family=EB+Garamond:wght@400;500&display=swap">
<style>
  :root {
    --backdrop: #eef3f3;
    --card-black: #050505;
    --card-glow: #3c3c3c;
    --ink-white: #ffffff;
    --ink-soft: #e6e6e6;
    --pattern-tone: rgba(255,255,255,0.06);
  }
  * { margin: 0; padding: 0; box-sizing: border-box; }
  html, body {
    width: 1200px; height: 516px; overflow: hidden;
    background: var(--backdrop);
    font-family: "EB Garamond", Garamond, serif;
  }
  .canvas {
    position: relative; width: 1200px; height: 516px;
    display: flex; justify-content: center; align-items: center; gap: 44px;
  }
  .card {
    position: relative; width: 500px; height: 290px;
    background: radial-gradient(ellipse at 45% 50%, var(--card-glow) 0%, #161616 45%, var(--card-black) 80%);
    overflow: hidden;
  }
  .card-front__pattern {
    position: absolute; inset: 0;
    background: radial-gradient(ellipse at 40% 45%, var(--pattern-tone), transparent 70%);
  }
  .brand-mark {
    position: absolute; left: 62px; top: 40px;
    width: 66px; height: 66px; border-radius: 50%;
    border: 2px solid var(--ink-white);
  }
  .company-name {
    position: absolute; left: 24px; top: 140px;
    color: var(--ink-white); font-size: 21px; font-weight: 400;
  }
  .company-cities {
    position: absolute; left: 28px; top: 176px;
    color: var(--ink-white); font-size: 13.5px; letter-spacing: 0.2px;
  }
  .person { position: absolute; left: 0; top: 56px; width: 456px; text-align: right; }
  .person-name { color: var(--ink-white); font-size: 20px; font-weight: 400; }
  .person-title { color: var(--ink-soft); font-size: 14px; margin-top: 10px; }
  .contact-strip { position: absolute; left: 268px; top: 165px; }
  .contact-email {
    position: absolute; left: 296px; top: 184px;
    color: var(--ink-white); font-size: 12.5px;
  }
  .contact-phone {
    position: absolute; left: 296px; top: 234px;
    color: var(--ink-white); font-size: 19px;
  }
  .card-back {
    background: radial-gradient(circle at 50% 50%, #5a5a5a 0%, #1e1e1e 40%, var(--card-black) 75%);
    display: flex; align-items: center; justify-content: center;
  }
  .back-seal {
    width: 190px; height: 190px; border-radius: 50%;
    border: 3px solid var(--ink-white);
    display: flex; align-items: center; justify-content: center; text-align: center;
    color: var(--ink-white); font-size: 18px; line-height: 1.3; padding: 20px;
  }
</style>
</head>
<body>
<main class="canvas">
  <section class="card card-front">
    <div class="card-front__pattern" role="img" aria-label="Faint repeating crest pattern across the card"></div>
    <div class="brand-mark" aria-hidden="true"></div>
    <p class="company-name">Dalvin Soeurs &amp; Company</p>
    <p class="company-cities">New York &bull; Los Angels &bull; Geneva</p>
    <div class="person">
      <p class="person-name">Dorian L. Dalvin</p>
      <p class="person-title">Chairman &amp; CEO</p>
    </div>
    <svg class="contact-strip" width="18" height="90" viewBox="0 0 18 90" aria-hidden="true">
      <rect x="0" y="0" width="18" height="90" rx="2" fill="#fff"/>
      <rect x="3" y="18" width="12" height="9" fill="none" stroke="#000" stroke-width="1.4"/>
      <polyline points="3,18 9,23 15,18" fill="none" stroke="#000" stroke-width="1.4"/>
      <rect x="5" y="66" width="8" height="14" rx="1.5" fill="none" stroke="#000" stroke-width="1.4"/>
      <rect x="7" y="68" width="4" height="4" fill="#000"/>
    </svg>
    <p class="contact-email">dorian@dalvinsoeurs.com</p>
    <p class="contact-phone">212.555.0148</p>
  </section>
  <section class="card card-back">
    <div class="back-seal">Dalvin Soeurs &amp; Company</div>
  </section>
</main>
</body>
</html>
```